TORNAVE5 Research Outcomes (e-Toolkit)

I would like you to design an electronic document that can be used to display the outcomes of the TORNAVE5 Research that can easily be downloaded from a website. This document will help nurses, educators, students and their supervisors to be able to better understand the outcomes of the research and apply it to their own practice. It should be something they can print out (A4 size) and refer to easily. It should be quite graphical and represent male and female nurses working in different specialty areas (emergency, primary healthcare, aged care, etc.), across hospital to primary healthcare (community) contexts. It should be professional, clean and crisp in appearance. There are areas in yellow in the attached document that are yet to be determined. All images within the document can be amended to better reflect the design of the document and the intent of its contained content. An example of the type of document I'm looking for is attached as "standards.pdf". It should be approximately 15 pages in length.
Updates

The project does not have to use the TORNAVE5 logo or its colours as a main design feature of the project.

Target Market(s)

Nurses, educators and students.

Industry/Entity Type

Education

Font styles to use
Sans Serif

Colors

Designer to choose colors to be used in the design.

Requirements
Must have
• Must have a diagram depicting the interrelatedness of all the individual metaspecialties. The contained diagrams can be modified to suit graphic design needs.
• Images of nursing professionals should appear Australian.
Nice to have
• I would like them to try and re-configure the diagrams as they are boring and I hate the colours. Images of collaboration amongst different healthcare team members would be nice.
Should not have
• Only images of female nurses or only images (if chosen) of nurses only working in a hospital.

```html
<!DOCTYPE html>
<html lang="en">
<head>
<meta charset="utf-8">
<title>TORNAVE5 Toolkit Cover Spread</title>
<link href="https://fonts.googleapis.com/css2?family=Oswald:wght@300;400;600&display=swap" rel="stylesheet">
<style>
  :root {
    --backdrop: #5a5a5a;
    --paper: #ffffff;
    --purple-light: #b3a5c8;
    --purple-mid: #8f7fa9;
    --purple-deep: #3d3056;
    --brand-purple: #5b3a8a;
    --green-light: #7cc48a;
    --green-dark: #5aab6a;
    --text-light: #ffffff;
  }
  html, body {
    margin: 0;
    padding: 0;
    width: 1200px;
    height: 824px;
    overflow: hidden;
    background: var(--backdrop);
  }
  .spread {
    display: block;
    width: 1200px;
    height: 824px;
    font-family: "Oswald", "Arial Narrow", sans-serif;
  }
  .paper { fill: var(--paper); }
  .photo-tone { fill: url(#photoTone); }
  .accent-wedge { fill: var(--purple-deep); }
  .green-panel { fill: url(#greenTone); }
  .cover-title { fill: var(--text-light); font-size: 26px; font-weight: 600; letter-spacing: 0.5px; }
  .cover-subtitle { fill: var(--text-light); font-size: 15px; font-weight: 300; letter-spacing: 0.4px; }
  .title-rule { stroke: var(--text-light); stroke-width: 1.2; }
  .authors-heading { fill: var(--text-light); font-size: 14px; font-weight: 600; letter-spacing: 0.5px; }
  .author-line { fill: var(--text-light); font-size: 11px; font-weight: 400; letter-spacing: 0.3px; }
  .funding-note { fill: var(--text-light); font-size: 12px; font-weight: 400; letter-spacing: 0.4px; }
  .project-number { fill: var(--text-light); font-size: 12px; font-weight: 600; letter-spacing: 0.4px; }
  .brand-name { fill: var(--brand-purple); font-size: 22px; font-weight: 600; letter-spacing: 0.5px; }
  .brand-dot { fill: var(--green-dark); }
  .spine-shade { fill: url(#spineShade); }
</style>
</head>
<body>
<svg class="spread" viewBox="0 0 1200 824" xmlns="http://www.w3.org/2000/svg">
  <defs>
    <linearGradient id="photoTone" x1="0" y1="0" x2="1" y2="1">
      <stop offset="0" stop-color="#8e7ea8"/>
      <stop offset="0.5" stop-color="#b3a5c8"/>
      <stop offset="1" stop-color="#a293ba"/>
    </linearGradient>
    <linearGradient id="greenTone" x1="0" y1="0" x2="1" y2="1">
      <stop offset="0" stop-color="#7cc48a"/>
      <stop offset="1" stop-color="#5aab6a"/>
    </linearGradient>
    <linearGradient id="spineShade" x1="0" y1="0" x2="1" y2="0">
      <stop offset="0" stop-color="#000" stop-opacity="0"/>
      <stop offset="0.5" stop-color="#000" stop-opacity="0.14"/>
      <stop offset="1" stop-color="#000" stop-opacity="0"/>
    </linearGradient>
  </defs>

  <!-- Back cover -->
  <g class="back-cover">
    <rect class="paper" x="63" y="32" width="537" height="760"/>
    <rect class="photo-tone" x="63" y="32" width="537" height="488" role="img" aria-label="Purple-toned photograph of a team reviewing charts and laptops around a desk"/>
    <path class="paper" d="M63,502 C250,484 450,384 600,320 L600,792 L63,792 Z"/>
    <path class="green-panel" d="M63,518 C250,500 450,400 600,336 L600,792 L63,792 Z"/>
    <text class="project-number" x="580" y="690" text-anchor="end">(PROJECT NUMBER DP240019385).</text>
    <text class="funding-note" x="95" y="724">THIS WORK WAS SUPPORTED BY</text>
    <text class="funding-note" x="95" y="742">THE NATIONAL HEALTH RESEARCH BOARD'S</text>
    <text class="funding-note" x="95" y="760">HORIZON PROJECTS FUNDING SCHEME</text>
  </g>

  <!-- Front cover -->
  <g class="front-cover">
    <rect class="photo-tone" x="600" y="32" width="537" height="460" role="img" aria-label="Purple-toned photograph of colleagues collaborating over reports, a tablet and a laptop"/>
    <path class="paper" d="M600,32 L1137,32 L1137,210 C950,190 760,120 600,70 Z"/>
    <path class="accent-wedge" d="M760,370 C900,420 1020,438 1137,440 L1137,470 C950,455 800,410 760,390 Z"/>
    <path class="paper" d="M600,320 C750,384 950,452 1137,466 L1137,792 L600,792 Z"/>
    <path class="green-panel" d="M600,336 C750,400 950,470 1137,490 L1137,792 L600,792 Z"/>

    <g class="brand-mark">
      <circle class="brand-dot" cx="990" cy="92" r="9"/>
      <text class="brand-name" x="1006" y="100">TORNAVE5</text>
    </g>

    <text class="cover-title" x="720" y="228">THE NURSE PRACTITIONER</text>
    <text class="cover-title" x="720" y="260">CLINICAL LEARNING AND TEACHING</text>
    <line class="title-rule" x1="720" y1="274" x2="1075" y2="274"/>
    <text class="cover-subtitle" x="720" y="298">A TOOLKIT FOR STUDENTS AND THEIR SUPERVISORS</text>

    <text class="authors-heading" x="640" y="562">AUTHORS:</text>
    <text class="author-line" x="648" y="584">DR MARA LINDQVIST, RN PHD HFACNP XX</text>
    <text class="author-line" x="648" y="599">PROFESSOR EMERITUS OWEN HALLOWAY RN PHD HFACNP XX</text>
    <text class="author-line" x="648" y="614">PROFESSOR RUTH PENHALE, RN PHD XX</text>
    <text class="author-line" x="648" y="629">MS DANA WHITCOMBE RN NP XX HFACNP</text>
    <text class="author-line" x="648" y="644">DR FELIX ARBUTHNOT RN NP PHD XX HFACNP</text>
  </g>

  <rect class="spine-shade" x="585" y="32" width="30" height="760"/>
</svg>
</body>
</html>
```